Pembrook Insurance Post Card

Specializing in “Towing & Transportation Insurance”
See our website at http://pembrookins-example.net/ for ideas on colors fonts etc.

Target Market(s)

Towing Companies

Font styles to use
Serif
Sans Serif

Requirements
Must have
• Specializing in “Towing & Transportation Insurance”
• Welcome to Pembrook Insurance:
• 2nd sentence (With our Agency, we work to make ourselves available to your business for when you need us most to keep your business moving forward.)
• 3rd Sentence: (Our customers were in mind when developing our agency and will continue to find new ways to make doing business with us easier.)
• We Offer: Change “Dealers Physical Damage” to “Auto Dealer Liability” & “Garage Liability” to “Garage Repair Liability”
• Our address: 718 Hollis Row NW, Suite F Decatur, AL 35988
• Email Address: PembrookInfo@velmarlink.example

```html
<!DOCTYPE html>
<html lang="en">
<head>
<meta charset="utf-8">
<title>Pembrook Insurance Postcard</title>
<link rel="stylesheet" href="https://fonts.googleapis.com/css2?family=Cinzel:wght@500&family=Barlow+Semi+Condensed:wght@500;600;700&family=Arimo:ital@1&display=swap">
<style>
  :root {
    --stage: #646567;
    --card: #ffffff;
    --gold: #8c6d3f;
    --gold-light: #b08a4f;
    --navy: #13285a;
    --blue-deep: #0c4a6e;
    --blue-mid: #0b6e9f;
    --blue-bright: #0a9fd6;
    --headline: #1d5f88;
    --body-dark: #1f3447;
    --white: #ffffff;
  }
  * { margin: 0; padding: 0; box-sizing: border-box; }
  html, body { width: 930px; height: 1200px; overflow: hidden; background: var(--stage); }
  .canvas { position: relative; width: 930px; height: 1200px; }
  .postcard {
    position: absolute; left: 105px; width: 717px; height: 522px;
    background: var(--card); overflow: hidden;
  }
  .postcard--front { top: 52px; }
  .postcard--back { top: 614px; }
  .postcard__art { position: absolute; inset: 0; }
  .brand-name {
    font-family: "Cinzel", serif; font-weight: 500; color: var(--navy);
    letter-spacing: 1.5px; white-space: nowrap; position: absolute;
  }
  .front-logo { position: absolute; left: 25px; top: 72px; width: 340px; height: 110px; }
  .front-logo .brand-name { left: 24px; top: 30px; font-size: 23px; }
  .front-logo .tagline {
    position: absolute; left: 26px; top: 70px;
    font-family: "Arimo", sans-serif; font-style: italic; font-size: 9.6px; color: var(--gold);
    white-space: nowrap;
  }
  .coverage-list {
    position: absolute; right: 52px; top: 206px; list-style: none; text-align: right;
    font-family: "Barlow Semi Condensed", sans-serif; font-weight: 600;
    font-size: 15px; line-height: 19.6px; color: var(--white);
  }
  .coverage-list__title { font-weight: 700; }
  .front-phone {
    position: absolute; right: 48px; top: 429px;
    font-family: "Barlow Semi Condensed", sans-serif; font-weight: 700;
    font-size: 33px; color: var(--white); letter-spacing: 0.5px;
  }
  .front-web {
    position: absolute; right: 52px; top: 472px;
    font-family: "Barlow Semi Condensed", sans-serif; font-weight: 600;
    font-size: 12.5px; color: var(--white);
  }
  .back-logo .brand-name { left: 50px; top: 56px; font-size: 21px; }
  .back-headline {
    position: absolute; left: 50px; top: 108px;
    font-family: "Barlow Semi Condensed", sans-serif; font-weight: 700;
    font-size: 29px; line-height: 36px; color: var(--headline); text-transform: uppercase;
  }
  .welcome {
    position: absolute; left: 50px; top: 268px; width: 245px;
    font-family: "Barlow Semi Condensed", sans-serif; font-weight: 500;
    font-size: 12.5px; line-height: 16px; color: var(--body-dark);
  }
  .welcome__title {
    font-weight: 700; font-size: 15px; line-height: 20px; color: var(--headline); margin-bottom: 4px;
  }
  .welcome p + p { margin-top: 6px; }
  .stamp-box {
    position: absolute; left: 586px; top: 68px; width: 66px; height: 80px;
    border: 1px solid rgba(255,255,255,0.8);
  }
  .mailing-address {
    position: absolute; right: 66px; top: 322px; text-align: right; font-style: normal;
    font-family: "Barlow Semi Condensed", sans-serif; font-weight: 600;
    font-size: 19px; line-height: 24px; color: var(--white);
  }
  .mailing-address__email { font-size: 15px; }
</style>
</head>
<body>
<main class="canvas">

  <section class="postcard postcard--front">
    <svg class="postcard__art" width="717" height="522" viewBox="0 0 717 522">
      <defs>
        <linearGradient id="front-photo" x1="0" y1="0" x2="1" y2="1">
          <stop offset="0" stop-color="#b7bcc2"/>
          <stop offset="0.35" stop-color="#d3d6d9"/>
          <stop offset="0.65" stop-color="#9da3a9"/>
          <stop offset="1" stop-color="#6f757b"/>
        </linearGradient>
        <linearGradient id="front-blue" x1="0" y1="0" x2="0" y2="1">
          <stop offset="0" stop-color="var(--blue-deep)"/>
          <stop offset="0.55" stop-color="var(--blue-mid)"/>
          <stop offset="1" stop-color="var(--blue-bright)"/>
        </linearGradient>
        <linearGradient id="gold-band" x1="0" y1="0" x2="0" y2="1">
          <stop offset="0" stop-color="var(--gold)"/>
          <stop offset="1" stop-color="var(--gold-light)"/>
        </linearGradient>
      </defs>
      <rect x="25" y="27" width="668" height="470" fill="url(#front-photo)" role="img" aria-label="Photo of a silver car being lifted by a tow truck on a street"/>
      <polygon points="537,27 693,27 693,497 311,497" fill="url(#front-blue)" role="img" aria-label="Blue-tinted photo of the rear of a tow truck"/>
      <polygon points="25,72 403,72 360,182 25,182" fill="#ffffff" opacity="0.92"/>
      <polygon points="433,0 550,0 311,497 299,522" fill="url(#gold-band)"/>
    </svg>
    <div class="front-logo">
      <span class="brand-name">PEMBROOK INSURANCE</span>
      <p class="tagline">Specializing in Towing &amp; Transportation Insurance</p>
    </div>
    <ul class="coverage-list">
      <li class="coverage-list__title">We Offer:</li>
      <li>Auto Liability</li>
      <li>General Liability</li>
      <li>Garage Repair Liability</li>
      <li>Garagekeepers</li>
      <li>Auto Dealer Liability</li>
      <li>OnHook</li>
      <li>Cargo</li>
      <li>Property Wrongful Repossession</li>
      <li>Umbrella/Excess</li>
      <li>Workers Compensation</li>
    </ul>
    <p class="front-phone">+334-555-0187</p>
    <p class="front-web">www.pembrookins-example.net</p>
  </section>

  <section class="postcard postcard--back">
    <svg class="postcard__art" width="717" height="522" viewBox="0 0 717 522">
      <defs>
        <linearGradient id="back-photo" x1="0" y1="0" x2="0" y2="1">
          <stop offset="0" stop-color="#eef0f2"/>
          <stop offset="0.45" stop-color="#d6dadf"/>
          <stop offset="0.7" stop-color="#c2c7cc"/>
          <stop offset="1" stop-color="#a4a8ac"/>
        </linearGradient>
        <linearGradient id="back-blue" x1="0" y1="0" x2="0" y2="1">
          <stop offset="0" stop-color="#0e4d74"/>
          <stop offset="1" stop-color="#126f9f"/>
        </linearGradient>
        <linearGradient id="gold-band-2" x1="0" y1="0" x2="0" y2="1">
          <stop offset="0" stop-color="var(--gold)"/>
          <stop offset="1" stop-color="var(--gold-light)"/>
        </linearGradient>
      </defs>
      <rect x="25" y="27" width="668" height="470" fill="url(#back-photo)" role="img" aria-label="Photo of a flatbed tow truck carrying an old car in front of mountains"/>
      <polygon points="537,27 693,27 693,497 311,497" fill="url(#back-blue)" role="img" aria-label="Blue-tinted photo of the flatbed tow truck and car"/>
      <polygon points="433,0 550,0 311,497 299,522" fill="url(#gold-band-2)"/>
    </svg>
    <div class="back-logo">
      <span class="brand-name">PEMBROOK INSURANCE</span>
    </div>
    <h1 class="back-headline">Specializing in<br>Towing &amp;<br>Transportation<br>Insurance</h1>
    <div class="welcome">
      <h2 class="welcome__title">Welcome to Pembrook Insurance:</h2>
      <p>With our Agency, we work to make ourselves available to your business for when you need us most to keep your business moving forward.</p>
      <p>Our customers were in mind when developing our agency and will continue to find new ways to make doing business with us easier.</p>
    </div>
    <div class="stamp-box" aria-label="Postage area"></div>
    <address class="mailing-address">
      Pembrook Insurance<br>
      718 Hollis Row NW, Suite F<br>
      Decatur, AL 35988<br>
      334-555-0187<br>
      <span class="mailing-address__email">PembrookInfo@velmarlink.example</span>
    </address>
  </section>

</main>
</body>
</html>
```